Iconic Australian Wine Brand looking for a complete brand makeover

- Require a new label design for the Clover Ridge range of wines
- Complete brand makeover with refreshed packaging design
- Inspiration for consumers to see the brand in a new light
- The final design should communicate fun, energetic and modern packaging with the aim of engaging our core target market of 20 - 35 year old female wine drinkers, while re-engaging our loyal female demographic of 35+ year olds.

Target Market(s)

Engage a Core target market of 20-35 year old female wine drinkers / secondary target market: re-engage our loyal female demographic of 35+ year olds

Requirements
Must have
• Complete brand makeover in order to re-engage our loyal female drinkers, now in their mid to late 30's
Nice to have
• Play on words for the Brand name

```html
<!DOCTYPE html>
<html lang="en">
<head>
<meta charset="utf-8">
<title>Clover Ridge — Wine Label Range</title>
<link rel="stylesheet" href="https://fonts.googleapis.com/css2?family=Playfair+Display:wght@400;700;900&family=Montserrat:wght@400;500&family=Sacramento&display=swap">
<style>
  :root {
    --paper: #f1eee8;
    --cream: #f3efe6;
    --night: #0d0d0d;
    --slate: #3b3b3c;
    --ink: #3a2a26;
    --white: #ffffff;
    --muted: #8a8580;
    --muted-light: #b9b9b9;
    --maroon: #7c1a24;
    --lime-1: #e8ec9a;
    --lime-2: #c9d045;
    --lime-3: #9fae3c;
    --pink-1: #f4a0b2;
    --pink-2: #e0305f;
    --pink-3: #b51d3c;
    --art-yellow: #c8b323;
    --art-red: #c8202c;
    --art-pink: #d61f66;
    --art-blue: #123f70;
  }
  * { box-sizing: border-box; margin: 0; padding: 0; }
  html, body { width: 1200px; height: 713px; overflow: hidden; }
  body { font-family: "Montserrat", sans-serif; }

  .range { display: flex; width: 1200px; height: 713px; }
  .panel { position: relative; height: 713px; display: flex; flex-direction: column; align-items: center; justify-content: center; gap: 12px; }
  .panel--white { width: 413px; background: var(--paper); }
  .panel--red { width: 379px; background: var(--night); }
  .panel--box { width: 408px; background: var(--paper); flex-direction: row; gap: 0; }

  /* Bottle labels */
  .label { width: 240px; height: 300px; display: flex; flex-direction: column; align-items: center; padding-top: 24px; }
  .label--white { background: var(--cream); color: var(--ink); }
  .label--red { background: var(--slate); color: var(--white); }

  .label__art { width: 110px; height: 68px; border-radius: 34px 34px 6px 6px; }
  .label--white .label__art { background: linear-gradient(90deg, var(--lime-1), var(--lime-2) 55%, var(--lime-3)); }
  .label--red .label__art { background: linear-gradient(90deg, var(--pink-1), var(--pink-2) 55%, var(--pink-3)); }

  .brand-name { font-family: "Playfair Display", serif; font-weight: 900; text-transform: uppercase; text-align: center; line-height: 0.92; letter-spacing: 1px; }
  .label .brand-name { font-size: 33px; margin-top: 16px; }
  .rule { height: 1px; background: currentColor; opacity: 0.7; }
  .label .rule { width: 150px; margin-top: 12px; }
  .varietal { font-family: "Playfair Display", serif; font-weight: 700; letter-spacing: 2.5px; text-transform: uppercase; }
  .label .varietal { font-size: 14px; margin-top: 14px; }
  .origin { font-size: 7px; letter-spacing: 1.2px; text-transform: uppercase; color: var(--muted); }
  .label .origin { margin-top: 16px; }
  .label--red .origin { color: var(--muted-light); }
  .vintage { font-family: "Playfair Display", serif; font-weight: 700; letter-spacing: 2px; }
  .label .vintage { font-size: 15px; margin-top: 12px; }

  .slogan-strip { width: 240px; height: 44px; display: flex; align-items: center; justify-content: center; border-top: 1px solid; border-bottom: 1px solid; }
  .slogan-strip--white { background: var(--cream); color: var(--ink); border-color: #a39d92; box-shadow: inset 0 3px 0 var(--cream), inset 0 -3px 0 var(--cream); }
  .slogan-strip--red { background: var(--slate); color: var(--white); border-color: #9a9a9a; }
  .slogan { font-family: "Sacramento", cursive; font-size: 22px; }

  /* Box, unfolded: front and side */
  .box-front, .box-side { height: 600px; background: #fbfaf7; position: relative; }
  .box-front { width: 200px; display: flex; flex-direction: column; align-items: center; color: var(--ink); }
  .box-side { width: 92px; border-left: 1px solid #e2ded6; padding: 18px 10px 0; color: var(--ink); }

  .box-front__art { width: 200px; height: 250px; background: linear-gradient(90deg, var(--art-yellow) 0%, var(--art-red) 30%, var(--art-pink) 58%, var(--art-blue) 85%, #fbfaf7 100%); }
  .box-front .brand-name { font-size: 27px; margin-top: 40px; }
  .box-front .rule { width: 110px; margin-top: 10px; }
  .box-front .varietal { font-size: 11px; margin-top: 80px; }
  .box-front .origin { font-size: 6px; margin-top: 12px; }
  .box-front .vintage { font-size: 11px; margin-top: 8px; }
  .box-front__band { width: 200px; height: 20px; background: var(--maroon); margin-top: 28px; }
  .box-front .slogan { font-size: 17px; margin-top: 14px; }

  .box-side .varietal { font-size: 8px; letter-spacing: 1px; }
  .box-side__copy { font-size: 6px; line-height: 1.6; margin-top: 10px; color: #5a504c; }
  .box-side__band { position: absolute; left: 0; top: 478px; width: 92px; height: 20px; background: var(--maroon); }
  .box-side__specs { position: absolute; left: 10px; right: 10px; top: 520px; display: flex; justify-content: space-between; font-family: "Playfair Display", serif; font-weight: 700; font-size: 9px; line-height: 1.1; }
</style>
</head>
<body>
<main class="range">

  <section class="panel panel--white">
    <div class="label label--white">
      <div class="label__art" role="img" aria-label="Illustration of four overlapping women's profiles in yellow-green tones"></div>
      <h1 class="brand-name">Clover<br>Ridge</h1>
      <div class="rule"></div>
      <p class="varietal">Chardonnay</p>
      <p class="origin">Made in Australia</p>
      <p class="vintage">· 2016 ·</p>
    </div>
    <div class="slogan-strip slogan-strip--white"><p class="slogan">Inspiring the moment</p></div>
  </section>

  <section class="panel panel--red">
    <div class="label label--red">
      <div class="label__art" role="img" aria-label="Illustration of four overlapping women's profiles in pink and red tones"></div>
      <h2 class="brand-name">Clover<br>Ridge</h2>
      <div class="rule"></div>
      <p class="varietal">Shiraz</p>
      <p class="origin">Made in Australia</p>
      <p class="vintage">· 2016 ·</p>
    </div>
    <div class="slogan-strip slogan-strip--red"><p class="slogan">Inspiring the moment</p></div>
  </section>

  <section class="panel panel--box">
    <div class="box-front">
      <div class="box-front__art" role="img" aria-label="Large illustration of overlapping women's profiles in yellow, red, pink and navy"></div>
      <h2 class="brand-name">Clover<br>Ridge</h2>
      <div class="rule"></div>
      <p class="varietal">Chardonnay</p>
      <p class="origin">Made in Australia</p>
      <p class="vintage">· 2016 ·</p>
      <div class="box-front__band"></div>
      <p class="slogan">Inspiring the moment</p>
    </div>
    <div class="box-side">
      <p class="varietal">Chardonnay</p>
      <p class="box-side__copy">A bright, crisp white with notes of citrus, green apple and soft stone fruit. Gently oaked for a creamy finish. Best enjoyed chilled with friends, seafood, salads or simply on its own as the sun goes down. Serve at eight to ten degrees.</p>
      <div class="box-side__band"></div>
      <div class="box-side__specs"><span>15%<br>VOL</span><span>750<br>ml</span></div>
    </div>
  </section>

</main>
</body>
</html>
```